packaging design for a hair accessories brand called TOVE NIK

Tove Nik is a premium hair accessories brand focused on elevated everyday style through beautifully crafted pieces that combine fashion, durability, and craftsmanship.

All products are handmade using high-quality materials and are designed to be exceptionally resistant, long-lasting, and almost unbreakable while still feeling elegant and refined.
The brand is not minimalist. Instead, it embraces a sophisticated and distinctive aesthetic with strong attention to detail, texture, shape, and presentation. The packaging and visual identity should feel modern, polished, feminine, and fashion-forward without looking overly simple or basic.Target customer:
Women 25–45 who care about personal style, quality, and details. They appreciate products that feel special, elevated, durable, and thoughtfully designed. They enjoy fashion and beauty products that look premium and giftable while remaining functional for everyday use.
The brand is for Mexico, so the text should be in spanish.
Brands for reference: Barovik, plindo, The curl fold
The visual identity should communicate:
Elegance
Premium craftsmanship
High quality
Durability
Sophistication
Modern femininity
Fashion-forward style
Boutique aesthetic

The packaging should feel:
Elegant and elevated
Visually rich and refined
Premium and giftable
Stylish and memorable
Sophisticated without being overly luxurious
Fashion-oriented and feminine
Designers should also develop a custom typography direction and logo treatment for the brand. The typography should feel distinctive, elegant, modern, and recognizable, helping create a strong brand identity that can extend across packaging, tags, and digital platforms.
The final visual identity should work cohesively across:
Hair accessory packaging
Hang tags
Product cards
Boxes and gift sets
E-commerce packaging
Social media and branding materials

I attach a packaging for reference. Use front and back. Measurments are: 10.5 xm x 13.5 cm

```html
<!DOCTYPE html>
<html lang="es">
<head>
<meta charset="utf-8">
<title>Tove Nik — Empaque frente y reverso</title>
<link rel="stylesheet" href="https://fonts.googleapis.com/css2?family=Michroma&display=swap">
<style>
  :root {
    --sheet: #ffffff;
    --sheet-edge: #3a3a3a;
    --ink: #000000;
    --type: #e6e6e6;
    --type-soft: #d2d2d2;
    --strand-green: #0f9a3c;
    --strand-mint: #7fbf98;
    --strand-pearl: #d9d9d9;
    --strand-rose: #c07878;
    --strand-red: #a80d0d;
    --strand-graphite: #4a4a4a;
  }
  * { margin: 0; padding: 0; box-sizing: border-box; }
  html, body { width: 1200px; height: 841px; overflow: hidden; background: var(--sheet); }
  .sheet {
    position: relative;
    width: 1200px; height: 841px;
    border: 1px solid var(--sheet-edge);
    background: var(--sheet);
    font-family: "Michroma", sans-serif;
  }
  .pack-face {
    position: absolute;
    top: 152px;
    width: 406px; height: 522px;
    background: var(--ink);
    border: 1px solid #222;
    overflow: hidden;
  }
  .pack-face--front { left: 164px; }
  .pack-face--back { left: 610px; }
  .strand-field { position: absolute; inset: 0; width: 100%; height: 100%; display: block; }
  .front-wordmark {
    position: absolute;
    right: 27px; bottom: 22px;
    font-size: 16px;
    letter-spacing: 0.5px;
    color: var(--type);
    line-height: 1;
  }
  .back-wordmark {
    position: absolute;
    top: 38px; left: 0; right: 0;
    text-align: center;
    font-size: 28px;
    letter-spacing: 1px;
    color: var(--type);
    line-height: 1;
  }
  .brand-values {
    position: absolute;
    top: 189px; left: 0; right: 0;
    list-style: none;
    text-align: center;
    font-size: 11.4px;
    line-height: 16px;
    color: var(--type-soft);
  }
</style>
</head>
<body>
<main class="sheet">
  <section class="pack-face pack-face--front" aria-label="Frente del empaque">
    <svg class="strand-field" role="img" aria-label="Patrón de mechones de cabello ondulados en verde, blanco y rojo sobre negro" viewBox="0 0 406 522" preserveAspectRatio="none">
      <defs>
        <linearGradient id="tricolor" x1="1" y1="0" x2="0" y2="1">
          <stop offset="0" stop-color="var(--strand-green)"/>
          <stop offset="0.28" stop-color="var(--strand-mint)"/>
          <stop offset="0.5" stop-color="var(--strand-pearl)"/>
          <stop offset="0.72" stop-color="var(--strand-rose)"/>
          <stop offset="1" stop-color="var(--strand-red)"/>
        </linearGradient>
        <radialGradient id="front-shade" cx="1" cy="1" r="0.75">
          <stop offset="0.35" stop-color="#000" stop-opacity="1"/>
          <stop offset="0.75" stop-color="#000" stop-opacity="0.35"/>
          <stop offset="1" stop-color="#000" stop-opacity="0"/>
        </radialGradient>
      </defs>
      <rect width="406" height="522" fill="url(#tricolor)" opacity="0.55"/>
      <rect width="406" height="522" fill="url(#front-shade)"/>
    </svg>
    <p class="front-wordmark">TOVE NIK</p>
  </section>

  <section class="pack-face pack-face--back" aria-label="Reverso del empaque">
    <svg class="strand-field" role="img" aria-label="Patrón de mechones de cabello ondulados en gris grafito sobre negro" viewBox="0 0 406 522" preserveAspectRatio="none">
      <defs>
        <radialGradient id="back-shade" cx="1" cy="1" r="0.7">
          <stop offset="0.3" stop-color="#000" stop-opacity="1"/>
          <stop offset="1" stop-color="#000" stop-opacity="0"/>
        </radialGradient>
      </defs>
      <rect width="406" height="522" fill="var(--strand-graphite)" opacity="0.5"/>
      <rect width="406" height="522" fill="url(#back-shade)"/>
    </svg>
    <h1 class="back-wordmark">TOVE NIK</h1>
    <ul class="brand-values">
      <li>ELEGANCIA</li>
      <li>ARTESANÍA DE PRIMERA CALIDAD</li>
      <li>ALTA CALIDAD</li>
      <li>DURABILIDAD</li>
      <li>SOFISTICACIÓN</li>
      <li>FEMINIDAD MODERNA</li>
      <li>ESTILO VANGUARDISTA</li>
      <li>ESTILO BOUTIQUE</li>
    </ul>
  </section>
</main>
</body>
</html>
```